Dodgeball League website

I require a nice, cool and attractive website for a new dodgeball league competition. I will need in PSD:

- Home Page
- Generic pages for news, about us etc
- Rank page with a table of team scores. stats etc

*Please design this with a Joomla*

I have attached:
- a logo
- site map for the links
- page layout guide

Example site for layout
http://www.velmorcircuit.com/

Design
Retro,cool feel, matches well with logo

Contact me if you have any questions

Reason: Would like to see a few more designs

Target Market(s)

Young adults 18 - 35.

Industry/Entity Type

News

Colors

Designer to choose colors to be used in the design.

Requirements
Must have
• I want a cool, retro feel to the website. Not to picky on the colors. Something that will match nicely with the logo given. I will give feedback on it.
Calm colors not too bright and overwhelming
Nice to have
• Include some pictures within the picture slider so I can get a feel for the website.
Nice clean background
Should not have
• To much clutter of text
Do not put pictures in the background.

```html
<!DOCTYPE html>
<html lang="en">
<head>
<meta charset="utf-8">
<title>Harbour Dodgeball League</title>
<link href="https://fonts.googleapis.com/css2?family=Ubuntu:wght@400;500;700&family=Ubuntu+Condensed&display=swap" rel="stylesheet">
<style>
:root{
  --bg:#262626;
  --page:#3b3b3b;
  --box:#1e1e1e;
  --cell:#161616;
  --orange:#f39a1c;
  --orange-dark:#e0561f;
  --text:#d8d8d8;
  --muted:#9a9a9a;
  --blue:#3f5d9c;
  --blue-dark:#324c86;
}
*{box-sizing:border-box;margin:0;padding:0}
html,body{width:673px;height:1200px;overflow:hidden}
body{background:radial-gradient(ellipse at 50% 30%,#3a3a3a,#1c1c1c 80%);font-family:"Ubuntu",sans-serif;color:var(--text);position:relative;font-size:8px}
.abs{position:absolute}
.logo{left:58px;top:10px;width:104px;height:92px;display:flex;align-items:center;gap:5px}
.logo .dot{width:22px;height:22px;border-radius:50%;background:var(--orange)}
.logo span{font-weight:700;font-size:12px;color:var(--orange);line-height:1.15}
.score{width:164px;height:49px;background:#1d1d1d;border:1px solid #333}
.score .hd{display:flex;justify-content:space-between;padding:3px 38px 3px 8px;color:var(--orange);font-size:6.5px;border-bottom:1px solid #2d2d2d}
.score .row{display:flex;font-size:6px;color:#999;border-bottom:1px solid #2a2a2a;height:16px;align-items:center}
.score .row b{flex:1;font-weight:400;padding-left:14px}
.score .row i{width:19px;text-align:center;font-style:normal;border-left:1px solid #2a2a2a;height:100%;line-height:16px}
.score-next{left:594px;top:13px;width:18px;height:106px;background:#1d1d1d;color:#888;font-size:9px;display:flex;align-items:center;justify-content:center}
.nav{left:58px;top:126px;width:556px;height:24px;background:var(--orange);display:flex;align-items:center;border:1px solid #c97810}
.nav a{font-size:8.5px;color:#3a1f00;padding:0 7px;height:100%;display:flex;align-items:center;border-right:1px solid #c97810;text-decoration:none;font-weight:500}
.nav a.on{background:var(--orange-dark);color:#fff}
.nav .search{margin-left:auto;margin-right:4px;width:115px;height:15px;background:#fff;border:1px solid #ccc;font-size:7px;color:#999;padding:3px 6px;position:relative}
.slider{left:56px;top:152px;width:561px;height:264px;background:#222;border:1px solid #555}
.slider .photo{position:absolute;inset:4px;background:linear-gradient(160deg,#6b7078 0%,#4a4f5a 40%,#b58b2a 70%,#2e2f36 100%)}
.slider .cap{position:absolute;left:4px;right:4px;bottom:4px;height:48px;background:rgba(0,0,0,.7);padding:8px 16px}
.slider .cap h2{color:var(--orange);font-size:15px;font-weight:700}
.slider .cap p{color:#ddd;font-size:9px;margin-top:3px}
.arrow{width:17px;height:17px;border-radius:50%;background:#ddd;display:inline-flex;align-items:center;justify-content:center}
.box{background:var(--box);border:1px solid #2c2c2c}
.box h3{color:var(--orange);font-size:12.5px;font-weight:500}
.news-item{font-size:7px;line-height:1.5;color:#ddd;padding-left:14px;position:relative;margin-bottom:8px}
.news-item:before{content:"›";position:absolute;left:4px;top:-2px;font-size:10px}
.news-item small{display:block;color:var(--muted);font-size:7px;margin-top:4px}
.fb-like{left:448px;top:433px;width:162px;height:80px;background:var(--blue);border:1px solid #5c78b4;text-align:center;color:#fff}
.register{left:448px;top:526px;width:162px;height:86px;background:var(--orange-dark);padding:8px}
.register .btn{position:absolute;left:5px;right:5px;bottom:6px;height:28px;background:linear-gradient(#ffcf3a,#f39a1c);border-radius:3px;color:#fff;font-size:13px;font-weight:500;display:flex;align-items:center;justify-content:center}
.tabs{display:flex;gap:26px;padding:8px 14px 0}
.tabs span{font-size:10.5px;color:#ccc;padding-bottom:6px}
.tabs span.on{color:var(--orange);border-bottom:2px solid var(--orange)}
.rank{display:flex;gap:4px;margin:0 14px 5px}
.rank .n{width:24px;height:25px;background:var(--cell);font-size:10px;display:flex;align-items:center;justify-content:center}
.rank .t{flex:1;background:var(--cell);font-size:7.5px;display:flex;align-items:center;padding-left:11px}
.rank .p{width:92px;background:var(--cell);display:flex;align-items:center;padding-left:9px;color:var(--orange);font-size:11px}
.rank .p em{font-style:normal;font-size:7px;margin-left:3px}
.rank .p em.w{color:#bbb}
.fb-find{left:448px;top:631px;width:162px;height:177px;background:var(--blue);border:1px solid #5c78b4;padding:6px}
.fb-grid{background:#fff;margin-top:6px;padding:4px;display:grid;grid-template-columns:repeat(4,1fr);gap:6px}
.fb-grid div{height:30px;background:linear-gradient(#cfd5de,#9aa4b4)}
.map-btn{left:448px;top:820px;width:162px;height:32px;background:var(--box);border:1px solid #2c2c2c;display:flex;align-items:center;gap:8px;padding-left:4px;font-size:10.5px;color:#eee}
.player{width:171px;height:74px;background:linear-gradient(#6f7a88,#4c5562);display:flex;padding:4px;gap:6px}
.player .ph{width:64px;height:64px;background:linear-gradient(#9aa3ad,#5f6670)}
.player p{font-size:7.5px;line-height:1.55;color:#fff}
.player p span{display:block;color:var(--orange)}
.partners{left:90px;top:1004px;width:490px;display:flex;justify-content:space-between}
.partners div{width:40px;height:18px;border-radius:3px;background:#5a5a5a}
.links{left:65px;top:1056px;color:var(--orange);font-size:8.5px}
.col{top:1076px;width:100px;font-size:7px;color:#999;line-height:14px;list-style:none}
.col li:before{content:"· "}
.flogo{left:506px;top:1058px;display:flex;align-items:center;gap:4px;width:70px;flex-wrap:wrap}
.flogo .dot{width:16px;height:16px;border-radius:50%;background:#888}
.flogo span{font-size:9px;font-weight:700;color:#aaa;line-height:1.1}
.social{left:472px;top:1129px;display:flex;gap:8px}
.social div{width:18px;height:18px;border-radius:3px}
.copy{left:0;top:1168px;width:673px;height:32px;background:#181818;text-align:center;font-size:7px;color:#999;line-height:32px}
</style>
</head>
<body>
<div class="abs logo"><div class="dot"></div><span>Harbour<br>Dodgeball<br>League</span></div>

<div class="abs score" style="left:254px;top:13px"><div class="hd"><span>Live Stream</span><span>Live Score</span></div><div class="row"><b>Nullam libero ero</b><i>3</i><i>6</i></div><div class="row"><b>Nullam libero eros convallis</b><i>3</i><i>6</i></div></div>
<div class="abs score" style="left:424px;top:13px"><div class="hd"><span>Live Stream</span><span>Live Score</span></div><div class="row"><b>Nullam libero ero</b><i>3</i><i>6</i></div><div class="row"><b>Nullam libero eros convallis</b><i>3</i><i>6</i></div></div>
<div class="abs score" style="left:254px;top:68px"><div class="hd"><span>Live Stream</span><span>Live Score</span></div><div class="row"><b>Nullam libero ero</b><i>3</i><i>6</i></div><div class="row"><b>Nullam libero eros convallis</b><i>3</i><i>6</i></div></div>
<div class="abs score" style="left:424px;top:68px"><div class="hd"><span>Live Stream</span><span>Live Score</span></div><div class="row"><b>Nullam libero ero</b><i>3</i><i>6</i></div><div class="row"><b>Nullam libero eros convallis</b><i>3</i><i>6</i></div></div>
<div class="abs score-next">›</div>

<nav class="abs nav">
  <a class="on">HOME</a><a>ABOUT</a><a>TEAMS</a><a>SCHEDULE</a><a>NEWS</a><a>PHOTOS AND VIDEOS</a><a>REGISTER</a><a>CONTACT US</a>
  <div class="search">Search<svg style="position:absolute;right:4px;top:3px" width="8" height="8" viewBox="0 0 8 8"><circle cx="3.2" cy="3.2" r="2.4" fill="none" stroke="#888" stroke-width="1"/><line x1="5" y1="5" x2="7.5" y2="7.5" stroke="#888"/></svg></div>
</nav>

<div class="abs" style="left:56px;top:152px;width:561px;height:890px;background:var(--page)"></div>

<div class="abs slider">
  <div class="photo" role="img" aria-label="Players throwing dodgeballs in an indoor sports hall"></div>
  <div class="cap">
    <h2>Fusce quis nisi dictum</h2>
    <p>Nam dapibus vehicula dolor, a iaculis nisl sodales</p>
    <div style="position:absolute;right:16px;top:16px;display:flex;gap:2px">
      <span class="arrow"><svg width="7" height="7" viewBox="0 0 7 7"><path d="M5 0.5L2 3.5L5 6.5" fill="none" stroke="#222" stroke-width="1.5"/></svg></span>
      <span class="arrow"><svg width="7" height="7" viewBox="0 0 7 7"><path d="M2 0.5L5 3.5L2 6.5" fill="none" stroke="#222" stroke-width="1.5"/></svg></span>
    </div>
  </div>
</div>

<section class="abs box" style="left:64px;top:432px;width:372px;height:181px">
  <div style="height:27px;background:#181818;padding:6px 14px;position:relative"><h3>Latest News</h3><span style="position:absolute;right:12px;top:8px;width:11px;height:11px;border-radius:50%;background:#ccc"></span></div>
  <div style="position:absolute;left:8px;top:38px;width:160px">
    <p class="news-item">Nullam libero eros, convallis id pharetra sed, tincidunt venenatis.<small>October 26, 2013</small></p>
    <p class="news-item">Nullam libero eros, convallis id pharetra sed, tincidunt venenatis.<small>October 26, 2013</small></p>
    <p class="news-item">Nullam libero eros, convallis id pharetra sed, tincidunt venenatis.<small>October 26, 2013</small></p>
  </div>
  <div style="position:absolute;left:186px;top:34px;width:1px;height:135px;background:#333"></div>
  <div role="img" aria-label="Dodgeball players on a gym court" style="position:absolute;left:203px;top:37px;width:159px;height:84px;border:2px solid #ddd;background:linear-gradient(#2a2b33,#4b4e58 55%,#a07a45)"></div>
  <p style="position:absolute;left:206px;top:131px;width:150px;font-size:7px;line-height:1.55;color:var(--orange)">Nullam libero eros, convallis id pharetra sed, tincidunt venenatis.<span style="display:block;color:#ddd;margin-top:4px">October 26, 2013</span></p>
</section>

<div class="abs fb-like">
  <p style="font-size:13px;margin-top:10px;letter-spacing:.5px">Like us on</p>
  <p style="font-size:15px;font-weight:700;margin-top:3px">Friendbook</p>
  <div style="position:absolute;left:0;right:0;bottom:0;height:12px;background:var(--blue-dark)"></div>
</div>

<div class="abs register">
  <div style="display:flex;gap:8px;align-items:center">
    <div style="width:44px;height:40px;border-radius:50%;background:#f6c24a;flex:none"></div>
    <p style="font-size:7px;line-height:1.6;color:#fff">Nullam libero eros, convallis id pharetra sed, tincidunt venenatis.</p>
  </div>
  <div class="btn">REGISTER NOW</div>
</div>

<section class="abs box" style="left:64px;top:631px;width:372px;height:221px">
  <div class="tabs"><span class="on">Ultimate Rubber League</span><span>Ultimate Foam League</span></div>
  <div style="height:1px;background:#333;margin:0 14px 13px"></div>
  <div class="rank"><div class="n">1</div><div class="t">Nullam libero eros, convallis id pharetra</div><div class="p">11,670<em>- Qualified</em></div></div>
  <div class="rank"><div class="n">1</div><div class="t">Nullam libero eros, convallis id pharetra</div><div class="p">11,670<em>- Qualified</em></div></div>
  <div class="rank"><div class="n">1</div><div class="t">Nullam libero eros, convallis id pharetra</div><div class="p">11,670<em class="w">- Withdraw</em></div></div>
  <div class="rank"><div class="n">1</div><div class="t">Nullam libero eros, convallis id pharetra</div><div class="p">11,670<em>- Qualified</em></div></div>
  <div class="rank"><div class="n">1</div><div class="t">Nullam libero eros, convallis id pharetra</div><div class="p">11,670<em>- Qualified</em></div></div>
  <p style="text-align:right;margin:12px 14px 0;font-size:7.5px;color:var(--muted)">Points at 25 Oct. Rankings FAQ | Velmor Circuit Race To Harbour</p>
</section>

<div class="abs fb-find">
  <p style="color:#fff;font-size:10px;padding-left:2px">Find us on <b style="font-size:15px">Friendbook</b></p>
  <div class="fb-grid" role="img" aria-label="Member profile thumbnails"><div></div><div></div><div></div><div></div><div></div><div></div><div></div><div></div><div></div><div></div><div></div><div></div></div>
  <p style="margin-top:9px;font-size:6px;color:#fff"><span style="background:#fff;color:var(--blue);padding:1px 3px">Like</span> <span style="background:#fff;color:#333;padding:1px 3px">3k</span></p>
</div>

<div class="abs map-btn">
  <svg width="32" height="32" viewBox="0 0 32 32"><rect x="1" y="1" width="30" height="30" rx="4" fill="#d9d4c4"/><path d="M16 6c-4 0-7 3-7 7 0 5 7 12 7 12s7-7 7-12c0-4-3-7-7-7z" fill="var(--orange-dark)"/><circle cx="16" cy="13" r="2.5" fill="#fff"/></svg>
  View our Location Map
</div>

<section class="abs box" style="left:64px;top:871px;width:546px;height:111px">
  <h3 style="text-align:center;font-size:11px;margin-top:9px">Top 3 Players</h3>
  <div style="position:absolute;left:9px;top:31px;display:flex;gap:8px">
    <div class="player"><div class="ph" role="img" aria-label="Top player portrait"></div><p>Nullam libero eros, convallis id pharetra sed, tincidunt venenatis.<span>Team name</span><span>Score</span></p></div>
    <div class="player"><div class="ph" role="img" aria-label="Top player portrait"></div><p>Nullam libero eros, convallis id pharetra sed, tincidunt venenatis.<span>Team name</span><span>Score</span></p></div>
    <div class="player"><div class="ph" role="img" aria-label="Top player portrait"></div><p>Nullam libero eros, convallis id pharetra sed, tincidunt venenatis.<span>Team name</span><span>Score</span></p></div>
  </div>
</section>

<div class="abs partners" aria-label="Partners"><div></div><div></div><div></div><div></div><div></div><div></div></div>

<p class="abs links">Quick Links</p>
<ul class="abs col" style="left:66px"><li>Integer lobortis</li><li>Curabitur ac</li><li>Phasellus tellus nisl</li><li>Aenean fringilla</li><li>Vestibulum</li><li>Aliquam commodo</li></ul>
<ul class="abs col" style="left:170px"><li>Integer lobortis</li><li>Curabitur ac</li><li>Phasellus tellus nisl</li><li>Aenean fringilla</li><li>Vestibulum</li><li>Aliquam commodo</li></ul>
<ul class="abs col" style="left:275px"><li>Integer lobortis</li><li>Curabitur ac</li><li>Phasellus tellus nisl</li><li>Aenean fringilla</li><li>Vestibulum</li><li>Aliquam commodo</li></ul>
<ul class="abs col" style="left:379px"><li>Integer lobortis</li><li>Curabitur ac</li><li>Phasellus tellus nisl</li><li>Aenean fringilla</li><li>Vestibulum</li><li>Aliquam commodo</li></ul>

<div class="abs flogo"><div class="dot"></div><span>Harbour Dodgeball League</span></div>
<div class="abs social"><div style="background:#3f5d9c"></div><div style="background:#3aa9e0"></div><div style="background:#1f77b4"></div><div style="background:#f07f1d"></div><div style="background:#d9493a"></div></div>

<div class="abs copy">Copyright © 2013 &nbsp; Harbour Dodgeball League. &nbsp; All rights reserved.</div>
</body>
</html>
```